Dog walking/Pet Sitting company needs a brochure to hook high end apartment tenants

We are looking for a brochure design that we can bring to meetings with high-end apartment and hotel management that will explain who we are, what we do, and how we can help their tenants/guests. I would like it to reflect the same look and feel of our website, carried over to printed brochure. Wesbite is www.hollowbrookpawcare.com. I can provide the stock images from the website if needed. A bi-fold brochure is ideal, unless you feel the information would fit better on a tri-fold. My company colors are #5D4664 and #5BA046. I would like a more professional tone to it, rather than fun.

Target Market(s)

Demo Professional Females and Males ages 30-50 with pets

Industry/Entity Type

Pet sitting

Font styles to use
Sans Serif

Colors
6b449b
9bcb3c

Requirements
Must have
• the same look and feel as my website; explain who we are, what we do, how we can help; include services offered; Mention that we service Parsippany and surrounding towns. Mention 15 years in business.
Should not have
• do not list pricing on brochure (you can mention pricing is available on the website). No cartoonish feel.

```html
<!DOCTYPE html>
<html lang="en">
<head>
<meta charset="utf-8">
<title>Hollowbrook Paw Care – Brochure Covers</title>
<link rel="stylesheet" href="https://fonts.googleapis.com/css2?family=Montserrat:wght@400;500;700&display=swap">
<style>
  :root {
    --stage: #2e2e2e;
    --green: #5ba046;
    --green-dark: #4f913c;
    --purple: #5d4664;
    --white: #ffffff;
    --paper: #f4f4f2;
  }
  * { box-sizing: border-box; margin: 0; padding: 0; }
  html, body { width: 1200px; height: 824px; overflow: hidden; }
  body {
    background: var(--stage);
    font-family: "Montserrat", Arial, sans-serif;
    color: var(--white);
  }
  .spread {
    position: absolute;
    left: 60px; top: 42px;
    width: 1080px; height: 740px;
    display: flex;
    box-shadow: 0 18px 40px rgba(0,0,0,.45);
  }
  .page {
    position: relative;
    width: 540px; height: 740px;
    overflow: hidden;
    background: var(--paper);
  }
  .photo { position: absolute; left: 0; top: 0; width: 540px; height: 500px; }
  .photo--back { background: linear-gradient(160deg, #8a9a5e 0%, #b7b4a8 40%, #6b6f70 75%, #4c4f52 100%); }
  .photo--front { background: linear-gradient(200deg, #eef0ef 0%, #d7c7b4 35%, #a7784f 60%, #e9e4de 100%); }
  .band { position: absolute; left: 0; top: 0; width: 540px; height: 740px; }
  .back-info {
    position: absolute; left: 0; right: 0; top: 532px;
    text-align: center;
  }
  .back-info__title { font-weight: 700; font-size: 15px; letter-spacing: .5px; margin-bottom: 12px; }
  .contact-line {
    display: flex; justify-content: center; align-items: center; gap: 6px;
    font-size: 11px; line-height: 20px;
  }
  .contact-line svg { width: 11px; height: 11px; }
  .reviews { font-size: 11px; margin-top: 6px; }
  .review-badges { display: flex; justify-content: center; gap: 10px; margin-top: 7px; }
  .review-badges span { width: 12px; height: 12px; border-radius: 50%; background: var(--white); }
  .site {
    position: absolute; left: 0; right: 0;
    text-align: center; font-size: 12px; letter-spacing: 4px;
  }
  .site--back { top: 700px; font-size: 13px; }
  .site--front { top: 660px; font-size: 11px; }
  .brand-seal {
    position: absolute; left: 200px; top: 408px;
    width: 140px; height: 140px; border-radius: 50%;
    background: var(--white);
    display: flex; align-items: center; justify-content: center;
    text-align: center;
  }
  .brand-seal__name {
    font-weight: 700; font-size: 15px; line-height: 19px; color: var(--green);
    text-transform: uppercase; letter-spacing: .5px;
  }
  .tagline { position: absolute; left: 0; right: 0; top: 572px; text-align: center; }
  .tagline__lead { font-weight: 500; font-size: 20px; }
  .tagline__main { font-weight: 700; font-size: 26px; margin-top: 4px; }
  .fold-corner {
    position: absolute; right: 0; top: 584px; width: 0; height: 0;
    border-left: 22px solid transparent; border-bottom: 22px solid var(--purple);
  }
</style>
</head>
<body>
  <main class="spread">
    <section class="page page--back">
      <div class="photo photo--back" role="img" aria-label="Photo of a white dog resting on a park path with its owners sitting behind"></div>
      <svg class="band" viewBox="0 0 540 740" aria-hidden="true">
        <path d="M0,492 Q270,452 540,360" fill="none" stroke="var(--purple)" stroke-width="6"/>
        <path d="M0,498 Q270,458 540,366 L540,740 L0,740 Z" fill="var(--green)"/>
      </svg>
      <div class="back-info">
        <h2 class="back-info__title">WE'D LOVE TO HELP YOU!</h2>
        <p class="contact-line">
          <svg viewBox="0 0 12 12"><circle cx="6" cy="6" r="5" fill="none" stroke="#fff" stroke-width="1.2"/><path d="M6 3v3l2 1.5" fill="none" stroke="#fff" stroke-width="1.2"/></svg>
          Mon-Fri: 8 am - 6 pm
        </p>
        <p class="contact-line">
          <svg viewBox="0 0 12 12"><path d="M3 1l2 3-1.2 1.2a6 6 0 0 0 3 3L8 7l3 2-1 2C5 11 1 7 1 2z" fill="#fff"/></svg>
          201-555-0148
        </p>
        <p class="contact-line">
          <svg viewBox="0 0 12 12"><rect x="1" y="2.5" width="10" height="7" fill="none" stroke="#fff" stroke-width="1.1"/><path d="M1 2.5l5 4 5-4" fill="none" stroke="#fff" stroke-width="1.1"/></svg>
          hello@hollowbrookpawcare.com
        </p>
        <p class="reviews">Check out our reviews on:</p>
        <div class="review-badges"><span></span><span></span><span></span></div>
      </div>
      <p class="site site--back">www.hollowbrookpawcare.com</p>
    </section>

    <section class="page page--front">
      <div class="photo photo--front" role="img" aria-label="Photo of a smiling woman hugging a fluffy Australian shepherd puppy"></div>
      <svg class="band" viewBox="0 0 540 740" aria-hidden="true">
        <path d="M0,492 Q270,486 540,440" fill="none" stroke="var(--purple)" stroke-width="6"/>
        <path d="M0,498 Q270,492 540,446 L540,740 L0,740 Z" fill="var(--green)"/>
      </svg>
      <div class="brand-seal">
        <p class="brand-seal__name">Hollowbrook<br>Paw Care</p>
      </div>
      <div class="tagline">
        <p class="tagline__lead">Prioritize Your Family.</p>
        <p class="tagline__main">We'll Focus on Your Pets.</p>
      </div>
      <p class="site site--front">www.hollowbrookpawcare.com</p>
      <div class="fold-corner"></div>
    </section>
  </main>
</body>
</html>
```